AI Startup Squarespace Website Design

I have a squarespace account setup with a domain name but need support to get the site looking good and launched. I will provide all text content and navigation/site map info. My company is working with clients to get business value out of Artificial Intelligence that helps automate processes, increase sales and improve customer customer experience. Leveraging the proven T.Helm AI Platform, our clients can get in-year benefits using customer service chatbots and other pre-built successful bots for automating/streamlining business processes in HR, accounting, underwriting, sales, training, remittances, emails, etc.

Target Market(s)

middle-market and large companies in Financial Services, Travel, Consumer Products, Manufacturing markets. Target is companies who want go improve sales, reduce costs and improve customer experience.

Industry/Entity Type

Financial

Font styles to use
Sans Serif

Requirements
Must have
• Professional but not too corporate-y.

```html
<!DOCTYPE html>
<html lang="en">
<head>
<meta charset="utf-8">
<title>Corvanta – Artificial Intelligence that helps Automate Processes</title>
<link href="https://fonts.googleapis.com/css2?family=Lato:wght@300;400;700&family=Crimson+Text:ital@1&display=swap" rel="stylesheet">
<style>
  :root {
    --ink: #2b2b2b;
    --text: #555555;
    --muted: #6d6e70;
    --accent: #1a8bcf;
    --rule: #b9b9b9;
    --hero-deep: #041a33;
    --hero-mid: #0b4f8a;
    --hero-glow: #2aa6e6;
    --paper: #ffffff;
  }
  * { margin: 0; padding: 0; box-sizing: border-box; }
  html, body { width: 765px; height: 1200px; overflow: hidden; background: var(--paper); }
  body { position: relative; font-family: "Lato", Arial, sans-serif; color: var(--text); }

  .site-header { position: absolute; top: 0; left: 0; width: 765px; height: 61px; }
  .brand { position: absolute; left: 75px; top: 11px; display: flex; align-items: center; gap: 8px; }
  .brand-mark { width: 14px; height: 14px; border-radius: 50%; background: var(--accent); }
  .brand-name { font-size: 30px; font-weight: 300; color: var(--muted); letter-spacing: 0.5px; line-height: 38px; }
  .main-nav { position: absolute; left: 268px; top: 26px; display: flex; gap: 14.5px; }
  .main-nav a { font-size: 8.6px; color: #444; text-decoration: none; letter-spacing: 0.2px; }

  .hero { position: absolute; top: 61px; left: 0; width: 765px; height: 379px;
    background: radial-gradient(ellipse at 48% 42%, var(--hero-glow) 0%, var(--hero-mid) 38%, var(--hero-deep) 100%); }
  .hero-title { position: absolute; top: 142px; left: 0; width: 765px; text-align: center;
    color: #fff; font-size: 27px; font-weight: 400; line-height: 30px; }

  .welcome { position: absolute; top: 478px; left: 0; width: 765px; text-align: center; }
  .welcome h1 { font-size: 24px; font-weight: 400; color: var(--ink); line-height: 30px; }
  .welcome p { font-size: 18px; font-weight: 400; color: var(--muted); line-height: 28px; }

  .rule { position: absolute; left: 75px; width: 615px; height: 1px; background: var(--rule); }

  .feature { position: absolute; top: 622px; width: 195px; }
  .feature h2 { font-size: 14.5px; font-weight: 400; color: var(--accent); margin-left: -3px; line-height: 20px; }
  .feature-photo { margin-top: 7px; width: 189px; height: 141px; }
  .feature p { margin-top: 16px; font-size: 8.8px; line-height: 14.6px; color: var(--text); }
  .btn { display: inline-block; border: 1.5px solid var(--accent); color: var(--accent);
    font-size: 8.6px; text-decoration: none; text-align: center; letter-spacing: 0.2px; }
  .feature .btn { margin-top: 16px; width: 87px; height: 27px; line-height: 24px; }

  .testimonial { position: absolute; top: 975px; left: 75px; width: 400px; }
  .testimonial blockquote { font-family: "Crimson Text", Georgia, serif; font-style: italic;
    font-size: 14px; line-height: 24px; color: #555; }
  .testimonial .btn { margin-top: 10px; width: 126px; height: 27px; line-height: 24px; }

  .quick-links { position: absolute; top: 981px; left: 574px; }
  .quick-links h3 { font-size: 10.5px; font-weight: 400; color: var(--ink); line-height: 16px; margin-bottom: 3px; }
  .quick-links a { display: block; font-size: 9.4px; color: var(--muted); text-decoration: none; line-height: 19.5px; }

  .site-footer { position: absolute; top: 1165px; left: 0; width: 765px; text-align: center;
    font-size: 9.4px; color: var(--muted); }
</style>
</head>
<body>
  <header class="site-header">
    <div class="brand"><span class="brand-mark"></span><span class="brand-name">corvanta</span></div>
    <nav class="main-nav">
      <a href="#">ABOUT US</a><a href="#">SERVICES</a><a href="#">WHY US</a><a href="#">CLIENTS</a><a href="#">SUPPORT</a><a href="#">TRAINING</a><a href="#">CONTACT</a>
    </nav>
  </header>

  <section class="hero" role="img" aria-label="Glowing blue circuit-board network forming an artificial intelligence brain">
    <h1 class="hero-title">Artificial Intelligence that helps<br>Automate Processes</h1>
  </section>

  <section class="welcome">
    <h1>Welcome to Corvanta</h1>
    <p>Morbi diam mauris viverra in gravida eu mattis</p>
  </section>

  <div class="rule" style="top:577px"></div>

  <article class="feature" style="left:75px">
    <h2>What We Do</h2>
    <div class="feature-photo" role="img" aria-label="Audience seated at a business conference facing a presentation screen" style="background:linear-gradient(135deg,#5a5e66,#c9c6c4 60%,#8b8e96)"></div>
    <p>Morbi diam mauris viverra in gravida eu mattis in ante Morbi eget arcu Morbi porta libero id ullamcorper nonummy nibh ligula</p>
    <a class="btn" href="#">MORE INFO</a>
  </article>

  <article class="feature" style="left:291px">
    <h2>Our Services</h2>
    <div class="feature-photo" role="img" aria-label="Hands working on a laptop with financial charts and a calculator on a desk" style="background:linear-gradient(135deg,#2c2c2e,#e8e8ea 55%,#b9c3cf)"></div>
    <p>Morbi diam mauris viverra in gravida eu mattis in ante Morbi eget arcu Morbi porta libero id ullamcorper nonummy nibh ligula</p>
    <a class="btn" href="#">MORE INFO</a>
  </article>

  <article class="feature" style="left:502px">
    <h2>Why We Are</h2>
    <div class="feature-photo" role="img" aria-label="Two colleagues smiling while reviewing work on a laptop in a bright office" style="background:linear-gradient(135deg,#d9dde2,#a98f7a 50%,#eef0f2)"></div>
    <p>Morbi diam mauris viverra in gravida eu mattis in ante Morbi eget arcu Morbi porta libero id ullamcorper nonummy nibh ligula</p>
    <a class="btn" href="#">MORE INFO</a>
  </article>

  <div class="rule" style="top:950px"></div>

  <section class="testimonial">
    <blockquote>“Vivamus porttitor purus nisi eleifend libero a tempus libero lectus feugiat felis Morbi diam mauris viverra in gravida eu mattis in ante Morbi eget arcu Morbi porta libero id ullamcorper ”</blockquote>
    <a class="btn" href="#">READ TESTIMONIAL</a>
  </section>

  <nav class="quick-links">
    <h3>Quick Links</h3>
    <a href="#">About Us</a><a href="#">Our Services</a><a href="#">Why Us</a><a href="#">Training</a><a href="#">Testimonials</a><a href="#">Contact Us</a>
  </nav>

  <div class="rule" style="top:1152px"></div>

  <footer class="site-footer">© 2018 Company Name&nbsp; All right reserved</footer>
</body>
</html>
```